Velvet Lantern rebranding my business with a new business card

I have my new logo and now I need a refresher on my business cards. I really want something fun and fresh. I like black background or anything to make the color pop.
Logo
Name: Velvet Lantern
Contact Info as stated below:
Mara Pelkin
519-555-0147
Logo
Name: Velvet Lantern
Mara Pelkin
519-555-0147
fb.me/VelvetLanternbyMara
Instagram: @VelvetLanternbyMara

Industry/Entity Type

Business

Contact Information for Business Card

double-sided. Logo on one side. Contact info on the other.

Requirements
Must have
• Logo
• Name: Velvet Lantern
• Contact Info as stated below:
• Mara Pelkin
• 519-555-0147
• fb.me/VelvetLanternbyMara
• fb.me/VelvetLanternbyMara

```html
<!DOCTYPE html>
<html lang="en">
<head>
<meta charset="UTF-8">
<title>Velvet Lantern — Business Card</title>
<link href="https://fonts.googleapis.com/css2?family=Josefin+Sans:wght@300&family=Pinyon+Script&display=swap" rel="stylesheet">
<style>
  :root {
    --backdrop: #3a312c;
    --card-black: #1c1a1b;
    --card-white: #ffffff;
    --ink-light: #f2f2f2;
    --brand-pink: #e99ac6;
    --brand-dark: #1c1a1b;
    --social-blue: #3b5998;
  }
  * { margin: 0; padding: 0; box-sizing: border-box; }
  html, body {
    width: 1200px; height: 1200px; overflow: hidden;
    background: var(--backdrop);
  }
  .sheet {
    width: 1200px; height: 1200px;
    display: flex; flex-direction: column;
    align-items: center; justify-content: center; gap: 60px;
  }
  .card {
    position: relative;
    width: 900px; height: 514px;
    overflow: hidden;
    background: var(--card-black);
    box-shadow: 0 10px 30px rgba(0,0,0,0.35);
  }
  .card-front {
    display: flex; align-items: center; justify-content: center;
  }
  .brand-mark {
    display: flex; align-items: center; gap: 16px;
    font-family: "Josefin Sans", sans-serif;
    font-weight: 300;
    font-size: 54px;
    letter-spacing: 2px;
    text-transform: uppercase;
    color: var(--brand-pink);
    white-space: nowrap;
  }
  .brand-dot {
    width: 26px; height: 26px; border-radius: 50%;
    background: var(--brand-pink);
  }
  .card-back .backdrop-shape {
    position: absolute; inset: 0;
  }
  .card-back .brand-mark {
    position: absolute; left: 50px; top: 236px;
    font-size: 34px;
    color: var(--brand-dark);
  }
  .card-back .brand-mark .brand-dot { background: var(--brand-dark); width: 18px; height: 18px; }
  .owner-name {
    position: absolute; right: 60px; top: 36px;
    font-family: "Pinyon Script", cursive;
    font-size: 54px;
    line-height: 1.2;
    color: var(--ink-light);
    white-space: nowrap;
  }
  .contact-list {
    position: absolute; right: 60px; bottom: 100px;
    list-style: none;
    font-family: "Josefin Sans", sans-serif;
    font-weight: 300;
    font-size: 20px;
    color: var(--ink-light);
    text-align: right;
    line-height: 1.6;
    white-space: nowrap;
  }
  .contact-list li { display: flex; justify-content: flex-end; align-items: center; gap: 12px; }
  .contact-list .business { text-transform: uppercase; padding-right: 46px; }
  .icon { width: 24px; height: 24px; flex: none; }
  .icon-social { width: 22px; height: 22px; background: var(--social-blue); border-radius: 3px; margin-right: 1px; }
</style>
</head>
<body>
<main class="sheet">
  <section class="card card-front" aria-label="Card front">
    <div class="brand-mark"><span class="brand-dot"></span>Velvet Lantern</div>
  </section>

  <section class="card card-back" aria-label="Card back">
    <svg class="backdrop-shape" viewBox="0 0 900 514" width="900" height="514" aria-hidden="true">
      <path d="M0 0 H380 C470 60 520 190 520 320 C520 410 500 470 480 514 H0 Z" fill="var(--card-white)"/>
      <path d="M360 18 C420 34 480 80 505 150 C470 100 420 55 360 18 Z" fill="var(--card-black)"/>
    </svg>
    <div class="brand-mark"><span class="brand-dot"></span>Velvet Lantern</div>
    <div class="owner-name">Mara Pelkin</div>
    <ul class="contact-list">
      <li class="business">Velvet Lantern</li>
      <li>519-555-0147
        <svg class="icon" viewBox="0 0 24 24" aria-hidden="true">
          <path d="M3 9 C3 5 21 5 21 9 L18 11 L16 8 H8 L6 11 Z" fill="var(--ink-light)"/>
          <path d="M7 12 H17 L19 20 H5 Z" fill="var(--ink-light)"/>
          <circle cx="12" cy="16" r="2" fill="var(--card-black)"/>
        </svg>
      </li>
      <li>fb.me/VelvetLanternbyMara <span class="icon icon-social"></span></li>
    </ul>
  </section>
</main>
</body>
</html>
```